Personalised Poetry business needs a business card designed

I am a writer that specialises in personalised poetry for people for significant life events.
I want a business card that stands out and portrays class and professionalism but is also welcoming & indicates warmth and honesty.
I'm happy with the logo that was designed for me, I would like to see it in raised print on the business card. I am open to suggestions on colours but think perhaps gold or silver writing for the logo would look good. I would like just the logo and my name and contact details on the front of the card. On the back of the card, I would like a list of the different events I provide poems for I will upload a photo of my current business card for reference. My current logo has a shading behind it that I don't like, I just want the words of the logo without any background colour

Target Market(s)

People wanting to provide a unique gift to someone special in their life

Industry/Entity Type

Writer

Contact Information for Business Card

Logo, my name and contact details on the front and a list of all the events I write poetry for on the back

Font styles to use
Script

Requirements
Must have
• I would like to see the logo, if possible, in a raised type of print on the card so that you can feel the actual words. I would like to have a glossy finish to the card and be able to print it on good quality board
Should not have
• The shading that is currently behind the logo on my current business card

```html
<!DOCTYPE html>
<html lang="en">
<head>
<meta charset="utf-8">
<title>Lasting Lines – Business Card</title>
<link rel="stylesheet" href="https://fonts.googleapis.com/css2?family=Libre+Baskerville:wght@700&family=Open+Sans:wght@400;600&family=Raleway:wght@400&display=swap">
<style>
  :root {
    --backdrop: #2b2c2e;
    --card: #1f1f21;
    --card-edge: #151516;
    --gold: #c9a045;
    --gold-soft: #8a6d33;
    --ink-light: #ecebe8;
  }
  * { box-sizing: border-box; margin: 0; padding: 0; }
  html, body { width: 1200px; height: 952px; overflow: hidden; }
  body {
    background: var(--backdrop);
    position: relative;
    font-family: "Open Sans", sans-serif;
  }
  .card {
    position: absolute;
    top: 326px;
    width: 520px;
    height: 300px;
    background: var(--card);
    border-radius: 16px;
    box-shadow: 0 3px 0 var(--card-edge), 0 6px 0 var(--card-edge), 0 18px 36px rgba(0,0,0,.45);
    overflow: hidden;
  }
  .card--front { left: 50px; }
  .card--back { left: 630px; }

  .brand { text-align: center; }
  .brand__name {
    font-family: "Libre Baskerville", serif;
    font-weight: 700;
    color: var(--gold);
    letter-spacing: 2px;
  }
  .brand__tagline {
    font-family: "Raleway", sans-serif;
    color: var(--gold-soft);
    letter-spacing: 1px;
  }
  .brand__dot {
    display: inline-block;
    width: 8px; height: 8px;
    border-radius: 50%;
    background: var(--gold);
    margin-top: 6px;
  }

  /* front */
  .card--front .brand { position: absolute; top: 48px; left: 0; right: 0; }
  .card--front .brand__name { font-size: 34px; }
  .card--front .brand__tagline { font-size: 15px; margin-top: 6px; }
  .rule {
    position: absolute;
    height: 1px;
    background: linear-gradient(90deg, transparent, var(--gold-soft) 15%, var(--gold-soft) 85%, transparent);
  }
  .card--front .rule--top { top: 150px; left: 40px; right: 40px; }
  .card--front .rule--bottom { top: 262px; left: 40px; right: 40px; }
  .holder-name {
    position: absolute;
    top: 166px; left: 0; right: 0;
    text-align: center;
    font-family: "Libre Baskerville", serif;
    font-weight: 700;
    font-size: 24px;
    letter-spacing: 2px;
    color: var(--gold);
  }
  .contacts {
    position: absolute;
    top: 216px; left: 0; right: 0;
    display: flex;
    justify-content: center;
    gap: 34px;
    list-style: none;
  }
  .contacts__item {
    display: flex; align-items: center; gap: 8px;
    color: var(--ink-light);
    font-size: 14px;
    font-weight: 600;
  }
  .contacts__icon {
    width: 18px; height: 18px;
    border-radius: 3px;
    background: var(--gold);
    display: flex; align-items: center; justify-content: center;
  }

  /* back */
  .card--back .brand { position: absolute; top: 30px; left: 0; right: 0; }
  .card--back .brand__name { font-size: 26px; }
  .card--back .brand__tagline { font-size: 12px; margin-top: 4px; }
  .services__title {
    position: absolute;
    top: 118px; left: 0; right: 0;
    text-align: center;
    font-family: "Libre Baskerville", serif;
    font-weight: 700;
    font-size: 17px;
    line-height: 1.45;
    letter-spacing: 1px;
    color: var(--gold);
  }
  .services {
    position: absolute;
    top: 188px; left: 24px; right: 24px;
    list-style: none;
    display: flex; flex-wrap: wrap; justify-content: center;
    column-gap: 16px; row-gap: 6px;
  }
  .services__item {
    display: flex; align-items: center; gap: 6px;
    color: var(--ink-light);
    font-size: 13px;
  }
  .services__break { flex-basis: 100%; height: 0; }
  .tick {
    width: 11px; height: 11px; border-radius: 50%;
    background: var(--gold);
    display: flex; align-items: center; justify-content: center;
  }
  .card--back .rule--top { top: 108px; left: 30px; right: 30px; }
  .card--back .rule--bottom { top: 272px; left: 30px; right: 30px; }
</style>
</head>
<body>

<section class="card card--front" aria-label="Business card front">
  <div class="brand">
    <div class="brand__name">LASTING LINES</div>
    <div class="brand__tagline">Personalised Poetry</div>
    <span class="brand__dot"></span>
  </div>
  <div class="rule rule--top"></div>
  <div class="holder-name">MARCUS ELWOOD</div>
  <ul class="contacts">
    <li class="contacts__item">
      <span class="contacts__icon">
        <svg width="11" height="11" viewBox="0 0 24 24"><path fill="#1f1f21" d="M6.6 10.8a15.1 15.1 0 0 0 6.6 6.6l2.2-2.2a1 1 0 0 1 1-.25 11.4 11.4 0 0 0 3.6.57 1 1 0 0 1 1 1V20a1 1 0 0 1-1 1A17 17 0 0 1 3 4a1 1 0 0 1 1-1h3.5a1 1 0 0 1 1 1c0 1.25.2 2.45.57 3.57a1 1 0 0 1-.25 1z"/></svg>
      </span>
      0400 000 123
    </li>
    <li class="contacts__item">
      <span class="contacts__icon">
        <svg width="11" height="11" viewBox="0 0 24 24"><path fill="#1f1f21" d="M3 5h18v14H3z"/><path fill="none" stroke="#c9a045" stroke-width="2" d="M3 6l9 7 9-7"/></svg>
      </span>
      marcus@lastinglines.com
    </li>
  </ul>
  <div class="rule rule--bottom"></div>
</section>

<section class="card card--back" aria-label="Business card back">
  <div class="brand">
    <div class="brand__name">LASTING LINES</div>
    <div class="brand__tagline">Personalised Poetry</div>
  </div>
  <div class="rule rule--top"></div>
  <h2 class="services__title">MOMENTOUS LIFE EVENTS PERSONALISED<br>IN POETRY</h2>
  <ul class="services">
    <li class="services__item"><span class="tick"><svg width="7" height="7" viewBox="0 0 10 10"><path d="M1.5 5.2l2.3 2.3L8.5 2.5" fill="none" stroke="#1f1f21" stroke-width="1.8"/></svg></span>Weddings &amp; Anniversaries</li>
    <li class="services__item"><span class="tick"><svg width="7" height="7" viewBox="0 0 10 10"><path d="M1.5 5.2l2.3 2.3L8.5 2.5" fill="none" stroke="#1f1f21" stroke-width="1.8"/></svg></span>Birthdays &amp; Christmas</li>
    <li class="services__item"><span class="tick"><svg width="7" height="7" viewBox="0 0 10 10"><path d="M1.5 5.2l2.3 2.3L8.5 2.5" fill="none" stroke="#1f1f21" stroke-width="1.8"/></svg></span>Valentines Day</li>
    <li class="services__break" aria-hidden="true"></li>
    <li class="services__item"><span class="tick"><svg width="7" height="7" viewBox="0 0 10 10"><path d="M1.5 5.2l2.3 2.3L8.5 2.5" fill="none" stroke="#1f1f21" stroke-width="1.8"/></svg></span>Retirements, Business &amp; Corporate Events</li>
    <li class="services__break" aria-hidden="true"></li>
    <li class="services__item"><span class="tick"><svg width="7" height="7" viewBox="0 0 10 10"><path d="M1.5 5.2l2.3 2.3L8.5 2.5" fill="none" stroke="#1f1f21" stroke-width="1.8"/></svg></span>Funerals &amp; Eulogies</li>
  </ul>
  <div class="rule rule--bottom"></div>
</section>

</body>
</html>
```